An internal sign in a physiotherapy clinic with gym. About working hard

We are a physiotherapy clinic / gym and we are wanting an internal wall to be a large sign with a great slogan
We are after 3 parts to it
1. The image / backdrop
2. The slogan
3. Our clinic logo

I have attached some images of the concept of what we are after. It can be climbing a mountain, rockclimbing and even hard work in a gym.

The slogan is:
"IF IT DOESN'T CHALLENGE YOU, IT WON'T CHANGE YOU"

Logo
I have attached a few different versions of our logo to assist you in the sign based on the background

THE SIGN SIZE WILL BE:
2935mm wide x 1885mm high

```html
<!DOCTYPE html>
<html lang="en">
<head>
<meta charset="utf-8">
<title>Challenge Wall Sign Concepts</title>
<link rel="stylesheet" href="https://fonts.googleapis.com/css2?family=Archivo+Black&family=Montserrat:wght@400&display=swap">
<style>
  :root{
    --stage:#111111;
    --white:#ffffff;
    --blue:#3cb6e3;
    --earth:#4a2c21;
    --band:#1b0e09;
    --ghost:#262626;
  }
  *{margin:0;padding:0;box-sizing:border-box}
  html,body{width:1200px;height:240px;overflow:hidden;background:var(--stage)}
  body{position:relative;font-family:"Archivo Black",sans-serif;color:var(--white)}
  .sign{position:absolute;top:40px;width:259px;height:166px;overflow:hidden}
  .sign--one{left:39px}
  .sign--two{left:307px}
  .sign--three{left:575px}
  .photo{position:absolute;inset:0}
  .sign--one .photo{background:linear-gradient(180deg,#6b5040 0%,#c98a4a 30%,#8a5a3c 55%,var(--earth) 75%,var(--earth) 100%)}
  .sign--two .photo{background:linear-gradient(180deg,#8a95b0 0%,#c9c3c8 38%,#e6c6a5 48%,#4b5a70 62%,#566d88 100%)}
  .sign--three .photo{top:55px;background:linear-gradient(180deg,#5a3a26 0%,#c9a27a 45%,#e9d9c2 70%,#b08a68 100%)}
  .band{position:absolute;left:0;right:0;top:0;height:55px;background:var(--band)}
  .brand{position:absolute;font-size:14px;letter-spacing:.5px;line-height:1;color:var(--white);white-space:nowrap}
  .sign--one .brand{left:18px;top:13px}
  .sign--two .brand{right:12px;top:14px}
  .sign--three .brand{left:172px;top:20px;font-size:16px}
  .slogan{position:absolute;line-height:1;white-space:nowrap}
  .slogan__lead{display:block;font-size:12.5px}
  .slogan__main{display:block;font-size:19px;letter-spacing:.3px}
  .slogan__tag{display:block;font-family:"Montserrat",sans-serif;font-weight:400;font-size:7.5px;letter-spacing:5px}
  .accent{color:var(--blue)}
  .sign--one .slogan{left:0;right:0;top:113px;text-align:center}
  .sign--one .slogan__main{margin-top:2px}
  .sign--one .slogan__tag{margin-top:4px;padding-left:5px}
  .sign--two .slogan{right:20px;top:105px;text-align:right}
  .sign--two .slogan__main{font-size:22px;margin-top:2px}
  .sign--two .slogan__tag{margin-top:3px;margin-right:-5px}
  .sign--two .divider{position:absolute;right:11px;top:106px;width:1.5px;height:40px;background:var(--white)}
  .sign--three .slogan{right:105px;top:13px;text-align:right}
  .sign--three .slogan__lead{display:inline-block;background:var(--blue);color:var(--white);font-size:8px;padding:1px 4px}
  .sign--three .slogan__main{font-size:14.5px;letter-spacing:0;margin-top:3px}
  .sign--three .slogan__tag{font-size:5px;letter-spacing:3px;margin-top:2px;margin-right:-3px}
  .sign--three .divider{position:absolute;left:159px;top:13px;width:1.5px;height:32px;background:var(--white)}
  .ghost-brand{position:absolute;left:990px;top:100px;font-size:36px;line-height:1;color:var(--ghost);letter-spacing:1px}
</style>
</head>
<body>
  <section class="sign sign--one">
    <div class="photo" role="img" aria-label="Climber scaling a rock face at sunset above misty mountain ridges"></div>
    <span class="brand">KOVA</span>
    <p class="slogan">
      <span class="slogan__lead">IF IT DOESN'T</span>
      <span class="slogan__main accent">CHALLENGE YOU</span>
      <span class="slogan__tag">IT WON'T CHANGE YOU</span>
    </p>
  </section>

  <section class="sign sign--two">
    <div class="photo" role="img" aria-label="Climber hanging from a rock overhang above the sea and an island at dusk"></div>
    <span class="brand">KOVA</span>
    <p class="slogan">
      <span class="slogan__lead">IF IT DOESN'T</span>
      <span class="slogan__main">CHALLENGE YOU</span>
      <span class="slogan__tag">IT WON'T CHANGE YOU</span>
    </p>
    <span class="divider"></span>
  </section>

  <section class="sign sign--three">
    <div class="band"></div>
    <div class="photo" role="img" aria-label="Climber reaching across a cave roof against a bright evening sky"></div>
    <p class="slogan">
      <span class="slogan__lead">IF IT DOESN'T</span>
      <span class="slogan__main"><span class="accent">CHALLENGE</span> YOU</span>
      <span class="slogan__tag">IT WON'T CHANGE YOU</span>
    </p>
    <span class="divider"></span>
    <span class="brand">KOVA</span>
  </section>

  <span class="ghost-brand">KOVA</span>
</body>
</html>
```